Training Consultant for Oil and Gas Drillers needs logo for business cards

I teach oil and gas professionals the skills required to keep rigs from blowing up. The company name is "Night Shift Bore Safety", which is pronounced Night Shyft. Tour refers to the time on an oil rig when a worker is off for sleep and rest. I teach something called Well Control, which is how to maintain a pressure balance in the well so the hydro carbons don't come to surface unexpectedly( like the Silver Tide Platform).

Target Market(s)

Rig hands and oil companies

Contact Information for Business Card

Night Shift BS ( company name) with a new logo
My name (Dale Ferrington )and Title (Well Control Consultant)
Phone number and address

Font styles to use
Serif
Sans Serif

Colors

Designer to choose colors to be used in the design.

Requirements
Must have
• I need a logo for the company. I do not have anything yet

```html
<!DOCTYPE html>
<html lang="en">
<head>
<meta charset="utf-8">
<title>Night Shift Bore Safety – Business Card</title>
<link href="https://fonts.googleapis.com/css2?family=Russo+One&family=Arimo:wght@400;700&display=swap" rel="stylesheet">
<style>
  :root {
    --stage: #2b2b2d;
    --card-dark: #0b0b0b;
    --card-light: #ffffff;
    --ink: #1a1a1a;
    --ink-soft: #2e2e2e;
    --silver: #c9c9c9;
    --accent: #e2471b;
    --accent-deep: #b3121b;
    --amber: #f2a21c;
    --faint-dark: #1c1c1c;
    --faint-light: #efefef;
  }
  * { margin: 0; padding: 0; box-sizing: border-box; }
  html, body { width: 1200px; height: 906px; overflow: hidden; }
  body {
    background: var(--stage);
    position: relative;
    font-family: "Arimo", Arial, sans-serif;
  }
  .card {
    position: absolute;
    width: 560px;
    height: 320px;
    border-radius: 18px;
    overflow: hidden;
    box-shadow: 0 14px 30px rgba(0,0,0,.45);
  }
  .card-front { left: 60px; top: 90px; background: var(--card-dark); }
  .card-back { left: 580px; top: 496px; background: var(--card-light); }

  .faint-mark {
    position: absolute;
    border-radius: 50%;
  }
  .card-front .faint-mark { width: 230px; height: 230px; right: 40px; top: -30px; background: var(--faint-dark); }
  .card-back .faint-mark { width: 170px; height: 170px; right: 60px; top: 22px; background: var(--faint-light); }

  .brand {
    position: absolute;
    display: flex;
    align-items: center;
    gap: 16px;
  }
  .brand-dot { border-radius: 50%; background: var(--accent); flex: none; }
  .brand-name {
    font-family: "Russo One", sans-serif;
    text-transform: uppercase;
    line-height: 1.02;
    letter-spacing: .5px;
  }
  .card-front .brand { left: 110px; top: 108px; }
  .card-front .brand-dot { width: 96px; height: 96px; }
  .card-front .brand-name { color: var(--silver); font-size: 34px; }

  .card-back .brand { left: 34px; top: 42px; }
  .card-back .brand-dot { width: 78px; height: 78px; }
  .card-back .brand-name { color: var(--ink); font-size: 27px; }

  .divider {
    position: absolute;
    left: 140px; right: 36px; top: 132px;
    height: 1px;
    background: var(--ink-soft);
  }
  .address {
    position: absolute;
    right: 40px; top: 142px;
    text-align: right;
    font-size: 14px;
    color: var(--ink);
    line-height: 1.35;
  }
  .person { position: absolute; left: 34px; top: 150px; }
  .person-name {
    font-family: "Russo One", sans-serif;
    font-size: 22px;
    color: var(--ink);
    text-transform: uppercase;
  }
  .person-title {
    font-family: "Russo One", sans-serif;
    font-size: 14px;
    color: var(--accent);
    text-transform: uppercase;
    letter-spacing: .6px;
    margin-top: 2px;
  }
  .contact { list-style: none; margin-top: 14px; }
  .contact li {
    display: flex; align-items: center; gap: 9px;
    font-size: 16px; color: var(--ink);
    margin-bottom: 6px;
  }
  .contact-icon {
    width: 20px; height: 20px; border-radius: 3px;
    background: var(--accent);
    display: flex; align-items: center; justify-content: center;
  }
  .wave { position: absolute; left: 0; bottom: 0; width: 560px; height: 140px; }
</style>
</head>
<body>

<section class="card card-front">
  <div class="faint-mark"></div>
  <div class="brand">
    <div class="brand-dot"></div>
    <div class="brand-name">Night Shift<br>Bore Safety</div>
  </div>
</section>

<section class="card card-back">
  <div class="faint-mark"></div>
  <div class="brand">
    <div class="brand-dot"></div>
    <div class="brand-name">Night Shift<br>Bore Safety</div>
  </div>
  <div class="divider"></div>
  <address class="address" style="font-style:normal">
    1875 Quarry Ridge Lane<br>
    Harlow Falls, WI 54990
  </address>
  <div class="person">
    <div class="person-name">Dale Ferrington</div>
    <div class="person-title">Well Control Consultant</div>
    <ul class="contact">
      <li>
        <span class="contact-icon">
          <svg width="12" height="12" viewBox="0 0 24 24"><path fill="#fff" d="M6.6 10.8a15 15 0 0 0 6.6 6.6l2.2-2.2c.3-.3.7-.4 1-.2 1.1.4 2.3.6 3.6.6.6 0 1 .4 1 1V20c0 .6-.4 1-1 1A17 17 0 0 1 3 4c0-.6.4-1 1-1h3.5c.6 0 1 .4 1 1 0 1.3.2 2.5.6 3.6.1.3 0 .7-.2 1z"/></svg>
        </span>
        (555) 418 2760
      </li>
      <li>
        <span class="contact-icon">
          <svg width="13" height="10" viewBox="0 0 26 20"><rect x="1.5" y="1.5" width="23" height="17" fill="none" stroke="#fff" stroke-width="2.5"/><path d="M2 2l11 9 11-9" fill="none" stroke="#fff" stroke-width="2.5"/></svg>
        </span>
        dale@nightshiftbs.com
      </li>
    </ul>
  </div>
  <svg class="wave" viewBox="0 0 560 140" preserveAspectRatio="none" aria-hidden="true">
    <defs>
      <linearGradient id="waveFire" x1="0" y1="1" x2="1" y2="0">
        <stop offset="0" stop-color="var(--accent-deep)"/>
        <stop offset=".55" stop-color="var(--accent)"/>
        <stop offset="1" stop-color="var(--amber)"/>
      </linearGradient>
      <linearGradient id="waveDeep" x1="0" y1="0" x2="1" y2="0">
        <stop offset="0" stop-color="#d81e1e"/>
        <stop offset="1" stop-color="#6e0a0d"/>
      </linearGradient>
    </defs>
    <path d="M0 118 C150 104 320 96 560 18 L560 140 L0 140 Z" fill="url(#waveFire)"/>
    <path d="M0 124 C180 118 360 110 560 40 L560 140 L0 140 Z" fill="#fff"/>
    <path d="M0 130 C200 128 380 118 560 58 L560 140 L0 140 Z" fill="url(#waveDeep)"/>
  </svg>
</section>

</body>
</html>
```